依頼詳細
■商品のアピールポイント・特徴
薬剤師が開発
ヨモギなど生薬が主成分
添加物不使用
発泡剤・界面活性剤・防腐剤・安定剤不使用
飲み込んでも安全
緑色のジェル
ミントの香り
価格 2000円前後予定

■商品のネーミング
Quoravelle (※読み方:クオラヴェル)

○ネーミング由来
pharmacist(薬剤師さん)+natural(自然派)+mint(ミントの香り)
女性らしいやさしい響きです。

■開発元会社紹介
110年続く漢方薬舗

■ターゲット(ペルソナ)
30〜50代女性

■パッケージデザイン
デザイン案の目安として、社内女性陣に多数決をおこなったところ、添付PDFのモノトーン系の①⑨⑤が好評でした。
また、商品写真を見ていただくと分かりますが、中身が緑色をしています。(わさびに似ていますが…)
また、商品名にもミントと付いていますので、デザインのベースはモノトーンでワンポイント的に緑があるのもいいかなと考えていますが、まだその辺りは未定です。
モノトーンのみのデザインでもデザインによっては良いかもしれません。

※商品名は必ずデザインに掲載お願い致します。英語表記限定→【Quoravelle】

■パッケージのポイント
ターゲットが女性で、ポーチの中で持ち歩き、外で友人の前で取り出したとしても恥ずかしくないデザイン。パッケージ自体は小さいので、化粧品のようなデザインでもアリかな。と考えています。

■お客様に与えたい印象
パッケージがおしゃれ。商品自体がおしゃれで気軽にポーチに持ち運べる。
薬剤師が開発した自然派の塗り薬だから安心して使える。

■ 重視する点/検討基準
何故そのデザインになったのか。その理由・ストーリー
記載項目
データでは、肩下サイズ60mmと記載されておりますが、
実際には88mmとなります。
肩下サイズは88mmにて作成下さいますようお願い申し上げます。
Φ19×88mm
添付資料の方御覧ください。
希望イメージ
シンプル 複雑
単色 カラフル
暗い 明るい
日常 高級
遊び心 厳粛
未来的 伝統的
女性的 男性的
希望する色
緑系、グレー系
納品ファイル
• 高解像度JPG (.jpg)
• イラストレーター形式 (.ai)
• フォトショップ形式 (.psd)
補足説明
パッケージ裏面には製品概要・成分表・弊社情報・連絡先等が入りますので、枠の作成をお願い致します。
依頼、デザインご提案の際に不備・疑問点などございましたら、お気軽にご連絡頂ければ幸いです。ご回答させていただきます。
すみません、提案数の関係で、提案の締め切りを少し延長させていただきます。
■ 選んだ理由

コンセプトとデザインが非常にマッチしており選ばせて頂きました!

■ 提案者全員のお礼・コメント

今回、沢山のご提案を頂きありがとうございました!
お陰様で良い商品になりそうです。
今後共よろしくお願い申し上げますm(_ _)m

```html
<!DOCTYPE html>
<html lang="en">
<head>
<meta charset="utf-8">
<title>Quoravelle Tube Label</title>
<link rel="stylesheet" href="https://fonts.googleapis.com/css2?family=Quicksand:wght@300;400;500&display=swap">
<style>
  :root {
    --paper: #ffffff;
    --tube-edge: #c9c9c9;
    --tube-mid: #ededed;
    --tube-light: #ffffff;
    --tube-line: #b5b5b5;
    --ink: #3a3a3a;
    --ink-soft: #4a4a4a;
    --ornament: #6e6e6e;
    --ornament-soft: #e3e3e3;
    --leaf: #3d8a3a;
    --leaf-light: #7cb86a;
  }
  * { margin: 0; padding: 0; box-sizing: border-box; }
  html, body {
    width: 1200px;
    height: 4148px;
    overflow: hidden;
    background: var(--paper);
  }
  .package {
    position: relative;
    width: 1200px;
    height: 4148px;
    background: var(--paper);
    color: var(--ink);
    font-family: "Quicksand", sans-serif;
    text-align: center;
  }
  .tube {
    position: absolute;
    inset: 0;
    width: 1200px;
    height: 4148px;
  }
  .copy {
    position: absolute;
    left: 200px;
    width: 800px;
    text-align: center;
    white-space: nowrap;
  }
  .tagline {
    top: 812px;
    font-size: 50px;
    font-weight: 400;
    line-height: 60px;
    color: var(--ink);
  }
  .brand-name {
    top: 872px;
    font-size: 150px;
    font-weight: 300;
    line-height: 170px;
    letter-spacing: 1px;
    color: var(--ink);
  }
  .claim {
    top: 1040px;
    font-size: 42px;
    font-weight: 400;
    line-height: 50px;
    color: var(--ink-soft);
  }
  .emblem {
    position: absolute;
    top: 1130px;
    left: 270px;
    width: 660px;
    height: 520px;
  }
  .flavour {
    top: 1712px;
    font-size: 50px;
    font-weight: 400;
    line-height: 60px;
    color: var(--ink-soft);
  }
  .divider {
    position: absolute;
    top: 2340px;
    left: 370px;
    width: 480px;
    height: 80px;
  }
  .features {
    top: 2540px;
    font-size: 52px;
    font-weight: 400;
    line-height: 60px;
    color: var(--ink);
    letter-spacing: -0.5px;
  }
  .features .star {
    display: block;
    font-size: 56px;
    line-height: 44px;
    color: var(--ink-soft);
  }
</style>
</head>
<body>
  <main class="package">
    <svg class="tube" viewBox="0 0 1200 4148" aria-hidden="true">
      <defs>
        <linearGradient id="tube-shade" x1="0" x2="1" y1="0" y2="0">
          <stop offset="0" stop-color="var(--tube-edge)"/>
          <stop offset="0.12" stop-color="var(--tube-mid)"/>
          <stop offset="0.45" stop-color="var(--tube-light)"/>
          <stop offset="0.85" stop-color="var(--tube-mid)"/>
          <stop offset="1" stop-color="var(--tube-edge)"/>
        </linearGradient>
      </defs>
      <!-- crimped seal -->
      <rect class="tube-seal" x="205" y="8" width="790" height="232" rx="14" fill="url(#tube-shade)" stroke="var(--tube-line)" stroke-width="3"/>
      <line x1="215" y1="200" x2="985" y2="200" stroke="var(--tube-line)" stroke-width="3"/>
      <!-- body -->
      <path class="tube-body" d="M210 240 L990 240 L945 3700 Q940 3760 900 3770 L300 3770 Q260 3760 255 3700 Z" fill="url(#tube-shade)" stroke="var(--tube-line)" stroke-width="3"/>
      <!-- cap -->
      <rect class="tube-cap" x="275" y="3770" width="650" height="370" rx="24" fill="url(#tube-shade)" stroke="var(--tube-line)" stroke-width="3"/>
      <line x1="280" y1="3790" x2="920" y2="3790" stroke="var(--tube-line)" stroke-width="3"/>
    </svg>

    <p class="copy tagline">A pharmacist develops it</p>
    <h1 class="copy brand-name">Quoravelle</h1>
    <p class="copy claim">Additive nonuse</p>

    <svg class="emblem" viewBox="0 0 660 520" role="img" aria-label="Ornate scrollwork frame around an oval medallion with a sprig of green mint leaves">
      <defs>
        <radialGradient id="scroll-tone" cx="0.5" cy="0.5" r="0.5">
          <stop offset="0.55" stop-color="var(--ornament-soft)"/>
          <stop offset="1" stop-color="var(--ornament-soft)" stop-opacity="0"/>
        </radialGradient>
        <radialGradient id="leaf-tone" cx="0.5" cy="0.5" r="0.5">
          <stop offset="0" stop-color="var(--leaf)"/>
          <stop offset="0.6" stop-color="var(--leaf-light)"/>
          <stop offset="1" stop-color="#ffffff"/>
        </radialGradient>
      </defs>
      <ellipse cx="330" cy="265" rx="330" ry="255" fill="url(#scroll-tone)"/>
      <ellipse cx="330" cy="270" rx="170" ry="205" fill="#ffffff" stroke="var(--ornament)" stroke-width="8"/>
      <ellipse cx="330" cy="270" rx="150" ry="185" fill="none" stroke="var(--ornament)" stroke-width="3"/>
      <ellipse cx="330" cy="275" rx="95" ry="125" fill="url(#leaf-tone)"/>
    </svg>

    <p class="copy flavour">Mint-flavored</p>

    <svg class="divider" viewBox="0 0 480 80" role="img" aria-label="Flourish divider with a small central ornament">
      <line x1="0" y1="40" x2="190" y2="40" stroke="var(--ornament)" stroke-width="4"/>
      <line x1="290" y1="40" x2="480" y2="40" stroke="var(--ornament)" stroke-width="4"/>
      <circle cx="4" cy="40" r="7" fill="var(--ornament)"/>
      <circle cx="476" cy="40" r="7" fill="var(--ornament)"/>
      <ellipse cx="240" cy="40" rx="42" ry="32" fill="var(--ornament-soft)"/>
    </svg>

    <p class="copy features">
      The crude drug including<br>
      the mugwort is a chief<br>
      ingredient
      <span class="star">*</span>
      Blowing agent, surfactant,<br>
      preservative, stabilizer<br>
      nonuse
      <span class="star">*</span>
      I am safe even if I swallow it
    </p>
  </main>
</body>
</html>
```